Life Coaching Business Card

Please check out my website at www.lorettavisbeck.com. Ideally I would like to use the same colors that I used on the site to match my business cards i.e: pink, green, teal, white
I want the final design to include a picture of me and also to be appealing and eye catching. For the picture I submitted, you can crop it smaller to just have my face (exclude my chest) showing.
Industry/Entity Type
Business
Contact Information for Business Card
Loretta Visbeck
Transformational Life Coach
web: www.lorettavisbeck.com
email: loretta@lorettavisbeck.com
Phone: 555-318-7042
Look and feel
Each slider illustrates characteristics of the customer's brand and the style your logo design should communicate.

```html
<!DOCTYPE html>
<html lang="en">
<head>
<meta charset="utf-8">
<title>Loretta Visbeck — Business Card</title>
<link rel="stylesheet" href="https://fonts.googleapis.com/css2?family=Tinos&display=swap">
<style>
  :root {
    --page: #ffffff;
    --magenta: #d02ef6;
    --lime: #66ff00;
    --ink: #ffffff;
    --portrait-light: #d9d9d9;
    --portrait-dark: #3a3a3a;
  }
  html, body {
    margin: 0;
    padding: 0;
    overflow: hidden;
  }
  body {
    width: 940px;
    height: 1200px;
    background: var(--page);
    position: relative;
    font-family: "Tinos", "Times New Roman", serif;
    color: var(--ink);
  }
  .card {
    position: absolute;
    left: 99px;
    width: 739px;
    background: var(--magenta);
    overflow: hidden;
  }
  .card--front {
    top: 81px;
    height: 429px;
  }
  .card--back {
    top: 529px;
    height: 427px;
  }
  .portrait {
    position: absolute;
    left: 0;
    top: 0;
    width: 282px;
    height: 100%;
    background: linear-gradient(100deg, var(--portrait-dark) 0%, #8a8a8a 35%, var(--portrait-light) 60%, #7a7a7a 100%);
  }
  .front-text {
    position: absolute;
    left: 282px;
    right: 0;
    top: 150px;
    text-align: center;
  }
  .name {
    margin: 0;
    font-weight: 400;
    font-size: 58px;
    line-height: 1;
    letter-spacing: -1.5px;
    transform: scaleX(0.86);
  }
  .title {
    margin: 16px 0 0;
    font-size: 26px;
    letter-spacing: -0.5px;
    transform: scaleX(0.88);
  }
  .panel {
    position: absolute;
    left: 34px;
    top: 32px;
    width: 670px;
    height: 362px;
    background: var(--lime);
    border-radius: 10px;
    text-align: center;
  }
  .panel .name {
    margin-top: 50px;
  }
  .web {
    margin: 18px 0 0;
    font-size: 19px;
    transform: scaleX(0.88);
  }
  .contact {
    position: absolute;
    left: 0;
    right: 0;
    top: 270px;
    font-size: 19px;
    line-height: 38px;
    transform: scaleX(0.88);
  }
  .contact p { margin: 0; }
</style>
</head>
<body>
  <section class="card card--front">
    <div class="portrait" role="img" aria-label="Black and white portrait photo of Loretta Visbeck"></div>
    <div class="front-text">
      <h1 class="name">Loretta Visbeck</h1>
      <p class="title">Transformational Life Coach</p>
    </div>
  </section>

  <section class="card card--back">
    <div class="panel">
      <h2 class="name">Loretta Visbeck</h2>
      <p class="web">web: www.lorettavisbeck.com</p>
      <div class="contact">
        <p>Phone: 555-318-7042</p>
        <p>email: loretta@lorettavisbeck.com</p>
      </div>
    </div>
  </section>
</body>
</html>
```